Stationery Design Project

We need, stationary designs for a store of children and juvenile furniture.
we have the logo. also need tags for the furniture with enought space to include description and options , maybe a 4" x 6" tag.

Target Market(s)

Parents of childrens and teens

Industry/Entity Type

Store

```html
<!DOCTYPE html>
<html lang="en">
<head>
<meta charset="utf-8">
<title>Nestwood Kids Letterhead</title>
<link rel="stylesheet" href="https://fonts.googleapis.com/css2?family=Roboto:wght@400;500&display=swap">
<style>
  :root {
    --backdrop: #e4e4e4;
    --paper: #f4f4f4;
    --teal: #69b6be;
    --ink: #6b6b6b;
    --rule: #8a8a8a;
  }
  * { margin: 0; padding: 0; box-sizing: border-box; }
  html, body {
    width: 1200px;
    height: 968px;
    overflow: hidden;
    background: var(--backdrop);
    font-family: "Roboto", Arial, sans-serif;
  }
  .letterhead {
    position: absolute;
    left: 282px;
    top: 34px;
    width: 636px;
    height: 900px;
    background: var(--paper);
    box-shadow: 0 2px 10px rgba(0,0,0,0.12);
    overflow: hidden;
  }
  .side-swoosh {
    position: absolute;
    left: 0;
    top: 0;
    width: 80px;
    height: 900px;
  }
  .brand {
    position: absolute;
    right: 60px;
    top: 62px;
    display: flex;
    align-items: center;
    gap: 10px;
  }
  .brand-mark {
    width: 22px;
    height: 22px;
    background: var(--teal);
  }
  .brand-name {
    font-size: 26px;
    font-weight: 500;
    color: var(--ink);
    letter-spacing: 1px;
    text-transform: uppercase;
  }
  .footer {
    position: absolute;
    left: 60px;
    right: 60px;
    bottom: 56px;
    text-align: center;
  }
  .footer-rule {
    border: 0;
    border-top: 1px solid var(--rule);
    margin-bottom: 14px;
  }
  .footer-line {
    font-size: 10px;
    line-height: 16px;
    color: var(--ink);
  }
  .footer-label {
    color: var(--teal);
    font-weight: 500;
  }
</style>
</head>
<body>
  <main class="letterhead">
    <svg class="side-swoosh" viewBox="0 0 80 900" aria-hidden="true">
      <path d="M0 150 C 60 300, 60 420, 0 560 L0 560 C 30 430, 30 290, 0 150 Z" fill="var(--teal)"/>
    </svg>

    <header class="brand">
      <span class="brand-mark"></span>
      <span class="brand-name">Nestwood Kids</span>
    </header>

    <footer class="footer">
      <hr class="footer-rule">
      <p class="footer-line">Harbour Lane, Millbrook NSW 2000 · <span class="footer-label">Tel:</span> +61 2 5550 0100 · <span class="footer-label">Fax:</span> +61 2 5550 0110</p>
      <p class="footer-line"><span class="footer-label">Email:</span> hello@nestwoodkids.com · www.nestwoodkids.com</p>
    </footer>
  </main>
</body>
</html>
```